Willowmere Spa and Beauty Ltd. (Name of business)

I need a business card designed for this new company based out of Toronto Ontario. We specialize in Eyelash Extensions, Manicures and Pedicures, body waxing, massages, laser hair removal and botox treatments. Also offer a variety of products for sale, such as skin cream serums, collagen gel, eye cream, etc. It is a safe relaxing and non-judgemental environnment. Clients are welcome to come be pampered for the half or full day. Many service packages to choose from.

Open 7days per week from 8am to 8pm.

Marissa Thornbury
Spa Facilitator
Willowmere Spa and Beauty Ltd.
7200 Calder Ave; Suite 1400
Toronto ON K8P 2W7

OFFICE: 416.739.4100
FAX: 416.739.4101
CELL: 416.582.6074
EMAIL: marissa.thornbury@willowmerespa.example

Target Market(s)

Target market is primarily female ranging from 16 years old to 50 years old.

Industry/Entity Type

Business

Contact Information for Business Card

Marissa Thornbury
Spa Facilitator
7200 Calder Ave; Suite 1400
Toronto ON K8P 2W7

OFFICE: 416.739.4100
FAX: 416.739.4101
CELL: 416.582.6074

Logo Text

I dont have a logo yet. I would like it simple but sophisticated and modern.

Font styles to use
Serif

Requirements
Must have
• all pertinent details such as company name, logo, name and contact information, services that are offered, including package rates
Nice to have
• Company name and logo prominent. A card that is neat and the information such as address, phone number, fax, email, etc is not too crowded but laid out in an easy to read format.
• Possibly on the back of card - some of the services offered could be listed, as well as professional cream lotions and serums. Hours of operation etc.

```html
<!DOCTYPE html>
<html lang="en">
<head>
<meta charset="utf-8">
<title>Willowmere Spa and Beauty Ltd. – Business Card</title>
<link rel="stylesheet" href="https://fonts.googleapis.com/css2?family=Tinos:wght@400;700&display=swap">
<style>
  :root {
    --ink: #231f20;
    --plum: #8a2a84;
    --sky: #74c3ef;
    --sky-light: #7cc4ee;
    --paper: #ffffff;
  }
  * { margin: 0; padding: 0; box-sizing: border-box; }
  html, body { width: 1200px; height: 1000px; overflow: hidden; background: var(--paper); }
  body { position: relative; font-family: "Tinos", "Times New Roman", serif; font-weight: 700; color: var(--ink); }

  .card { position: absolute; left: 253px; width: 694px; border: 2px solid var(--ink); background: var(--paper); overflow: hidden; }
  .card--front { top: 68px; height: 425px; }
  .card--back { top: 508px; height: 425px; }

  .front__head { position: absolute; left: 0; top: 0; width: 100%; height: 180px; }
  .front__rule { position: absolute; left: 0; top: 178px; width: 100%; height: 4px; background: var(--ink); }
  .front__band { position: absolute; left: 0; top: 185px; width: 100%; height: 240px; background: var(--sky); }

  .identity { position: absolute; left: 0; top: 90px; width: 100%; height: 32px; display: flex; align-items: center; justify-content: center; gap: 14px; }
  .identity__mark { width: 22px; height: 22px; background: var(--sky-light); }
  .identity__name { color: var(--plum); font-size: 27px; line-height: 32px; }

  .details { position: absolute; left: 26px; top: 72px; font-size: 18px; line-height: 23.5px; }
  .divider { position: absolute; left: 301px; top: 67px; width: 3px; height: 105px; background: var(--ink); }

  .contacts { position: absolute; left: 334px; top: 72px; list-style: none; font-size: 18px; line-height: 23.5px; }
  .contacts li { display: flex; align-items: center; height: 23.5px; }
  .contacts svg { width: 22px; height: 20px; margin-right: 4px; flex: none; }
  .contacts .sep { font-weight: 400; margin-right: 6px; }
  .contacts .email { font-size: 15.5px; }

  .hours { position: absolute; left: 0; top: 0; width: 100%; height: 100%; }
  .hours__word { position: absolute; font-size: 34px; top: 158px; }
  .hours__open { left: 180px; }
  .hours__days { left: 415px; }
  .hours__ring { position: absolute; left: 290px; top: 116px; width: 116px; height: 116px; border: 4px solid var(--sky-light); border-radius: 50%; }
  .hours__seven { position: absolute; left: 286px; top: 118px; width: 124px; text-align: center; font-size: 100px; line-height: 110px; }
  .hours__week { position: absolute; left: 0; width: 100%; top: 236px; text-align: center; font-size: 25px; word-spacing: 4px; }
  .hours__time { position: absolute; left: 0; width: 100%; top: 281px; text-align: center; font-size: 25px; }
</style>
</head>
<body>

<section class="card card--front" aria-label="Card front">
  <div class="front__head">
    <div class="identity">
      <span class="identity__mark" aria-hidden="true"></span>
      <span class="identity__name">MARISSA THORNBURY</span>
    </div>
  </div>
  <div class="front__rule"></div>
  <div class="front__band">
    <p class="details">
      Spa Facilitator<br>
      Willowmere Spa and Beauty Ltd.<br>
      7200 Calder Ave; Suite 1400<br>
      Toronto ON K8P 2W7
    </p>
    <div class="divider"></div>
    <ul class="contacts">
      <li>
        <svg viewBox="0 0 22 20" aria-label="Office"><circle cx="11" cy="10" r="8.5" fill="none" stroke="var(--plum)" stroke-width="1.6"/><path d="M7.5 6.5c1-1 1.8-.6 2.3.5l.3.8c.2.6-.5 1-.7 1.3.6 1.4 1.4 2.2 2.6 2.8.4-.3.8-.9 1.4-.6l.8.4c1 .5 1.2 1.3.3 2.2-1.8 1.6-7.8-3.4-7-7.4z" fill="var(--plum)"/></svg>
        <span class="sep">:</span>416.739.4100
      </li>
      <li>
        <svg viewBox="0 0 22 20" aria-label="Fax"><rect x="6" y="2" width="10" height="6" fill="none" stroke="var(--plum)" stroke-width="1.5"/><rect x="3" y="8" width="16" height="8" rx="1.5" fill="var(--plum)"/><rect x="7" y="13" width="8" height="5" fill="var(--plum)" stroke="#fff" stroke-width="1"/></svg>
        <span class="sep">:</span>416.739.4101
      </li>
      <li>
        <svg viewBox="0 0 22 20" aria-label="Cell"><rect x="7" y="2" width="8" height="16" rx="1.5" fill="none" stroke="var(--plum)" stroke-width="1.5"/><rect x="8.5" y="4" width="5" height="5" fill="var(--plum)"/><rect x="8.5" y="11" width="5" height="5" fill="var(--plum)" opacity=".5"/></svg>
        <span class="sep">:</span>416.582.6074
      </li>
      <li>
        <svg viewBox="0 0 22 20" aria-label="Email"><rect x="3" y="5" width="16" height="11" fill="var(--plum)"/><path d="M3 5l8 6 8-6" fill="none" stroke="#fff" stroke-width="1.2"/></svg>
        <span class="sep">:</span><span class="email">marissa.thornbury@willowmerespa.example</span>
      </li>
    </ul>
  </div>
</section>

<section class="card card--back" aria-label="Card back">
  <div class="hours">
    <span class="hours__word hours__open">OPEN</span>
    <span class="hours__ring" aria-hidden="true"></span>
    <span class="hours__seven">7</span>
    <span class="hours__word hours__days">DAYS</span>
    <p class="hours__week">PER WEEK</p>
    <p class="hours__time">FROM 8AM TO 8PM.</p>
  </div>
</section>

</body>
</html>
```